Stationery & Business Card Design Project

We require our stationary to be professional, which will stand out but also be sophisticated and reputable.

We also require the following:

* Business card must be double sided
* Logo must stand out with brightnest colours used. Other colours may be added but only in small doses as not to overtake the main colours.
* For business card brightnest pty ltd smsf specialists with administrators at bottom left on the front of the card and details on the back

Industry/Entity Type

Business

Requirements
Must have
• * Business Cards
* With compliments slips –2 different ones
* Forwarding mail slip (smaller version of a with compliments slip)

```html
<!DOCTYPE html>
<html lang="en">
<head>
<meta charset="utf-8">
<title>brightnest business card</title>
<link rel="stylesheet" href="https://fonts.googleapis.com/css2?family=Source+Sans+3:wght@400;600&display=swap">
<style>
  :root {
    --navy: #2b3480;
    --navy-deep: #1f2468;
    --grey: #8b8b8e;
    --grey-light: #d4d4d6;
    --ink: #3a3a3c;
    --card: #ffffff;
    --backdrop: #ecebe8;
  }
  * { margin: 0; padding: 0; box-sizing: border-box; }
  html, body {
    width: 1200px; height: 989px; overflow: hidden;
    background: var(--backdrop);
    font-family: "Source Sans 3", sans-serif;
  }
  .stage { position: relative; width: 1200px; height: 989px; }
  .card {
    position: absolute; width: 751px; height: 428px;
    background: var(--card); overflow: hidden;
    box-shadow: 0 4px 14px rgba(0,0,0,0.18);
  }
  .card--front { left: 44px; top: 31px; border-radius: 0 26px 0 26px; }
  .card--back { left: 403px; top: 530px; border-radius: 0 26px 0 26px; }
  .edge-panel { position: absolute; inset: 0; }
  .brand-mark { position: absolute; background: var(--navy); border-radius: 6px; }
  .brand-name {
    position: absolute; color: var(--navy); font-weight: 600;
    letter-spacing: -1.5px; line-height: 1;
  }
  .brand-tagline {
    position: absolute; color: var(--grey); font-size: 13px;
    letter-spacing: 7px; font-weight: 600;
  }
  .card--front .brand-mark { left: 42px; top: 274px; width: 120px; height: 120px; }
  .card--front .brand-name { left: 176px; top: 294px; font-size: 70px; }
  .card--front .brand-tagline { left: 182px; top: 366px; }
  .card--back .brand-mark { left: 119px; top: 136px; width: 170px; height: 168px; }
  .card--back .brand-name { left: 52px; top: 308px; font-size: 70px; }
  .card--back .brand-tagline { left: 56px; top: 380px; }
  .name-bar {
    position: absolute; left: 443px; top: 136px; width: 262px; height: 82px;
    background: linear-gradient(90deg, var(--navy-deep), var(--navy));
    color: #fff; padding: 12px 10px;
  }
  .name-bar .person { font-size: 27px; font-weight: 600; line-height: 1.1; }
  .name-bar .role { font-size: 18px; }
  .accent-tab {
    position: absolute; left: 720px; top: 136px; width: 31px; height: 82px;
    background: linear-gradient(90deg, var(--grey), var(--grey-light));
  }
  .contact {
    position: absolute; left: 450px; top: 237px;
    font-size: 18.5px; color: var(--ink); line-height: 25px;
  }
  .contact-rows { display: grid; grid-template-columns: 66px auto; margin-top: 2px; }
  .contact-rows dt { color: var(--navy); }
  .contact-rows dd.web { font-weight: 600; }
</style>
</head>
<body>
<main class="stage">
  <section class="card card--front" aria-label="Card front">
    <svg class="edge-panel" viewBox="0 0 751 428" width="751" height="428" aria-hidden="true">
      <path fill="var(--navy)" d="M690 0 L751 0 L751 428 L560 428 Q735 260 690 0 Z"/>
    </svg>
    <div class="brand-mark" aria-hidden="true"></div>
    <div class="brand-name">brightnest</div>
    <div class="brand-tagline">smsf specialists</div>
  </section>

  <section class="card card--back" aria-label="Card back">
    <div class="brand-mark" aria-hidden="true"></div>
    <div class="brand-name">brightnest</div>
    <div class="brand-tagline">smsf specialists</div>
    <div class="name-bar">
      <div class="person">Your Name here</div>
      <div class="role">Director</div>
    </div>
    <div class="accent-tab" aria-hidden="true"></div>
    <div class="contact">
      <p>48 Harbour Lane, Suite 210</p>
      <p>Northbay, NB 20417</p>
      <dl class="contact-rows">
        <dt>Phone</dt><dd>021.555.0142</dd>
        <dt>Cell</dt><dd>021.555.0142</dd>
        <dt>Fax</dt><dd>021.555.0142</dd>
        <dt>Email</dt><dd>hello@brightnest.example</dd>
        <dt>Web</dt><dd class="web">www.brightnest.example</dd>
      </dl>
    </div>
  </section>
</main>
</body>
</html>
```